New Silver Crest Cards

We are a high end restroom trailer company. Please see our website for our design and exactly what we do.
silvercrestrestrooms.com
See tan back ground on the website. We would like to use that as the background. Also we would like to add 1 or two photos of the interior of our restroom trailers to the back of the card.

Also we would like the business card adjustable since I need to buy for other employees in my business. Marcus Hollwick with cell 301-555-0142 and Trevor Denbury with cell 301-555-0187. All the other information is the same as mine.

It Company

Deirdre Hollwick
(301) 555-0163 office
(301) 555-0129 cell
dee@silvercrestrestrooms.com
SilverCrestRestrooms.com

```html
<!DOCTYPE html>
<html lang="en">
<head>
<meta charset="utf-8">
<title>Silver Crest Restroom Trailers – Business Cards</title>
<link href="https://fonts.googleapis.com/css2?family=Marcellus+SC&family=EB+Garamond:ital,wght@0,400;1,400&display=swap" rel="stylesheet">
<style>
  :root {
    --page-bg: #d9d6d1;
    --card-tan: #e4d4a8;
    --card-tan-light: #ebdfba;
    --brand-blue: #1b7cc6;
    --ink-brown: #5a4a2c;
    --rule-grey: #a89a78;
  }
  * { box-sizing: border-box; margin: 0; padding: 0; }
  html, body { width: 1200px; height: 800px; overflow: hidden; }
  body {
    background: var(--page-bg);
    display: flex;
    align-items: center;
    justify-content: center;
    gap: 40px;
  }
  .card {
    position: relative;
    width: 560px;
    height: 320px;
    background: linear-gradient(160deg, var(--card-tan-light), var(--card-tan));
    box-shadow: 0 10px 28px rgba(0,0,0,.25);
    overflow: hidden;
  }

  /* brand lockup */
  .brand {
    position: absolute;
    display: flex;
    align-items: center;
    gap: 14px;
  }
  .brand-dot {
    width: 62px; height: 62px;
    border-radius: 50%;
    background: var(--brand-blue);
    flex: none;
  }
  .brand-text { display: flex; flex-direction: column; }
  .brand-name {
    font-family: "Marcellus SC", serif;
    font-size: 34px;
    line-height: 1;
    color: var(--brand-blue);
    letter-spacing: .5px;
  }
  .brand-sub {
    font-family: "Marcellus SC", serif;
    font-size: 17px;
    color: var(--brand-blue);
    letter-spacing: 1px;
    margin-top: 2px;
    padding-bottom: 3px;
    border-bottom: 1px solid var(--rule-grey);
  }
  .brand-tagline {
    font-family: "EB Garamond", serif;
    font-style: italic;
    font-size: 15px;
    color: var(--ink-brown);
    margin-top: 3px;
  }

  /* front */
  .card-front .brand { top: 44px; left: 150px; }
  .holder-name {
    position: absolute;
    top: 150px; left: 38px;
    font-family: "Marcellus SC", serif;
    font-size: 21px;
    color: var(--brand-blue);
  }
  .contact-list {
    position: absolute;
    top: 192px; left: 300px;
    list-style: none;
    font-family: "EB Garamond", serif;
    font-size: 17px;
    color: var(--brand-blue);
    line-height: 1.35;
  }
  .contact-list li { display: flex; align-items: center; gap: 8px; }
  .contact-list svg { width: 14px; height: 14px; flex: none; fill: var(--brand-blue); }

  /* back */
  .card-back .brand { top: 22px; left: 210px; }
  .card-back .brand-dot { width: 52px; height: 52px; }
  .card-back .brand-name { font-size: 28px; }
  .card-back .brand-sub { font-size: 14px; }
  .card-back .brand-tagline { font-size: 13px; }
  .photo-band {
    position: absolute;
    left: 0; right: 0;
    top: 118px; height: 150px;
    background: var(--brand-blue);
    padding: 8px 0;
    display: flex;
    gap: 6px;
  }
  .photo { flex: 1; height: 100%; }
  .photo-stalls { background: linear-gradient(135deg, #d9c27a, #a77a3c 60%, #f0ead4); }
  .photo-wood { background: linear-gradient(135deg, #6d6a66, #8a5b2c 55%, #b88347); }
  .photo-vanity { background: linear-gradient(135deg, #e7eeea, #c9d8d2 50%, #8f7a5a); }
</style>
</head>
<body>

  <section class="card card-back">
    <div class="brand">
      <span class="brand-dot"></span>
      <div class="brand-text">
        <span class="brand-name">Silver Crest</span>
        <span class="brand-sub">Restroom Trailers</span>
        <span class="brand-tagline">Make Every Event Shine!</span>
      </div>
    </div>
    <div class="photo-band">
      <div class="photo photo-stalls" role="img" aria-label="Photo of a restroom trailer interior with urinals and wood floor"></div>
      <div class="photo photo-wood" role="img" aria-label="Photo of a restroom trailer interior with wood stall doors and vanity"></div>
      <div class="photo photo-vanity" role="img" aria-label="Photo of a bright restroom trailer interior with white vanity and sinks"></div>
    </div>
  </section>

  <section class="card card-front">
    <div class="brand">
      <span class="brand-dot"></span>
      <div class="brand-text">
        <span class="brand-name">Silver Crest</span>
        <span class="brand-sub">Restroom Trailers</span>
        <span class="brand-tagline">Make Every Event Shine!</span>
      </div>
    </div>
    <p class="holder-name">Deirdre Hollwick</p>
    <ul class="contact-list">
      <li>
        <svg viewBox="0 0 24 24" aria-hidden="true"><path d="M6.6 10.8a15 15 0 0 0 6.6 6.6l2.2-2.2a1 1 0 0 1 1-.25 11.4 11.4 0 0 0 3.6.6 1 1 0 0 1 1 1V20a1 1 0 0 1-1 1A17 17 0 0 1 3 4a1 1 0 0 1 1-1h3.5a1 1 0 0 1 1 1c0 1.250.2 2.450.6 3.6a1 1 0 0 1-.25 1z"/></svg>
        (301) 555-0163
      </li>
      <li>
        <svg viewBox="0 0 24 24" aria-hidden="true"><path d="M7 1h10a2 2 0 0 1 2 2v18a2 2 0 0 1-2 2H7a2 2 0 0 1-2-2V3a2 2 0 0 1 2-2zm0 3v14h10V4zm5 15.2a1 1 0 1 0 0 2 1 1 0 0 0 0-2z"/></svg>
        (301) 555-0129
      </li>
      <li>
        <svg viewBox="0 0 24 24" aria-hidden="true"><path d="M2 5h20v14H2zm2 2v.5l8 5 8-5V7zm0 2.8V17h16V9.8l-8 5z"/></svg>
        dee@silvercrestrestrooms.com
      </li>
      <li>
        <svg viewBox="0 0 24 24" aria-hidden="true"><path d="M12 2a10 10 0 1 0 0 20 10 10 0 0 0 0-20zm6.9 9h-3a15 15 0 0 0-1.3-6 8 8 0 0 1 4.3 6zM12 4c.9 1.2 1.7 3.7 1.9 7h-3.8c.2-3.3 1-5.8 1.9-7zM9.4 5a15 15 0 0 0-1.3 6h-3a8 8 0 0 1 4.3-6zM5.1 13h3a15 15 0 0 0 1.3 6 8 8 0 0 1-4.3-6zM12 20c-.9-1.2-1.7-3.7-1.9-7h3.8c-.2 3.3-1 5.8-1.9 7zm2.6-1a15 15 0 0 0 1.3-6h3a8 8 0 0 1-4.3 6z"/></svg>
        SilverCrestRestrooms.com
      </li>
    </ul>
  </section>

</body>
</html>
```